Portal Panel Medic need professional looking business card printed on plastic, Commericial, Industri

We are family owned and operated garage door company in Indianapolis, Indiana. We sale service and install dock equipment, doors, operators. We are looking to expand our commercial/ industrial division. We also service all residential doors and operators. We are looking for a business that stands out of the crowd. We are committed to have the best customer service in the industry.

Target Market(s)

National and local general contractors, National/ Corpate service accounts,

Industry/Entity Type

Business Service

Contact Information for Business Card

To be printed on plastic stock

Font styles to use
Sans Serif

Colors
ffffff
f04a50
ec1f27

Requirements
Must have
• Name, website,email, phone number, position.
Nice to have
• A standout professional design

```html
<!DOCTYPE html>
<html lang="en">
<head>
<meta charset="utf-8">
<title>Portal Panel Medic – Business Card</title>
<link rel="stylesheet" href="https://fonts.googleapis.com/css2?family=Arimo:wght@400;700&display=swap">
<style>
  :root {
    --page: #e9e6e2;
    --card-light: #ffffff;
    --card-dark: #000000;
    --brand-red: #ec1f27;
    --brand-red-soft: #f04a50;
    --ink: #3a3a3a;
    --rule: #9a9a9a;
    --white: #ffffff;
  }
  * { box-sizing: border-box; margin: 0; padding: 0; }
  html, body { width: 1200px; height: 960px; overflow: hidden; }
  body {
    background: var(--page);
    font-family: "Arimo", Arial, sans-serif;
    position: relative;
  }
  .card {
    position: absolute;
    left: 248px;
    width: 703px;
    height: 400px;
    border-radius: 28px;
    box-shadow: 0 6px 18px rgba(0,0,0,0.18);
  }
  .card--front { top: 60px; background: var(--card-light); }
  .card--back { top: 500px; background: var(--card-dark); }

  .brand-name {
    position: absolute;
    color: var(--brand-red);
    font-weight: 700;
    text-transform: uppercase;
    line-height: 0.95;
    letter-spacing: -0.5px;
  }
  .card--front .brand-name { left: 62px; top: 138px; font-size: 44px; }
  .card--back .brand-name {
    left: 0; right: 0; top: 108px;
    text-align: center; font-size: 58px;
  }

  .divider {
    position: absolute;
    left: 352px; top: 78px;
    width: 1.5px; height: 246px;
    background: var(--rule);
  }

  .details { position: absolute; left: 396px; top: 72px; color: var(--ink); }
  .person-name { color: var(--brand-red); font-weight: 700; font-size: 24px; line-height: 1.2; }
  .person-role { font-size: 19px; line-height: 1.3; }
  .contact-list { list-style: none; margin-top: 20px; }
  .contact-list li {
    display: flex; align-items: center;
    font-size: 16px; line-height: 23px;
  }
  .contact-list svg { width: 14px; height: 14px; margin-right: 12px; flex: none; }
  .company { color: var(--brand-red); font-weight: 700; font-size: 16.5px; margin-top: 19px; line-height: 22px; }
  .address { font-style: normal; font-size: 16.5px; line-height: 22px; }

  .back-url {
    position: absolute; left: 0; right: 0; top: 312px;
    text-align: center;
    color: var(--white);
    font-size: 16px;
    letter-spacing: 3.4px;
  }
  .back-url .accent { color: var(--brand-red-soft); }
</style>
</head>
<body>
  <section class="card card--front">
    <div class="brand-name">Portal<br>Panel<br>Medic</div>
    <div class="divider"></div>
    <div class="details">
      <div class="person-name">Daniel Whitcombe</div>
      <div class="person-role">President &amp; CEO</div>
      <ul class="contact-list">
        <li>
          <svg viewBox="0 0 14 14" aria-hidden="true"><path d="M9 1.5 C12 4 11 10 4 12.5 L3 10.8 C6.5 9.5 8.5 6.5 7.6 3 Z" fill="var(--brand-red)"/></svg>
          555.014.2287
        </li>
        <li>
          <svg viewBox="0 0 14 14" aria-hidden="true"><rect x="1" y="3" width="12" height="8.5" fill="none" stroke="var(--brand-red)" stroke-width="1.4"/><path d="M1 3.5 L7 8 L13 3.5" fill="none" stroke="var(--brand-red)" stroke-width="1.4"/></svg>
          info@portalpanelmedic.com
        </li>
        <li>
          <svg viewBox="0 0 14 14" aria-hidden="true"><g fill="none" stroke="var(--brand-red)" stroke-width="1.1"><circle cx="7" cy="7" r="5.8"/><ellipse cx="7" cy="7" rx="2.6" ry="5.8"/><path d="M1.2 7 H12.8 M2 4 H12 M2 10 H12"/></g></svg>
          www.portalpanelmedic.com
        </li>
      </ul>
      <div class="company">Portal Panel Medic</div>
      <address class="address">2140 Meridian Street<br>Suite 310<br>Indianapolis, IN 46202</address>
    </div>
  </section>

  <section class="card card--back">
    <div class="brand-name">Portal<br>Panel<br>Medic</div>
    <div class="back-url">www.<span class="accent">portalpanelmedic</span>.com</div>
  </section>
</body>
</html>
```